Swimming Pool Service Website needed!!!

Hi Everyone! Thanks for looking at my contest. I PROMISE to provide excellent feedback during this process.

I am starting a new swimming pool business cleaning company in San Diego, California and would like your help in making it similar to one of these two websites that are already functioning.

http://www.brightlagoonworks.example/services-repair.html

http://tidemarkaquacare.example/commercial-pool-cleaning.php

I like these two because they are easy to read, classy, sophisticated and have nice pictures of really clean & clear pools.

I really like the blue on white color format.

I do not have a logo, but the name of my company is GLIMMERWAVE POOL SERVICE.

My tag line is: Water so pure, it sparkles like a summer sky. (does not need to have the quotes around "in"...maybe just italics for this word IN?) You decide for me.

I would like to have a logo designed that incorporates some sort of easy to read letters. I do not want cursive (handwriting) letters. I thought about having a "reflection" of letters (mirror image), but think that this will be hard to read from far away. Maybe you can surprise me and come up with an idea that works using the a mirror image....but I'm not sure. I was leaning toward plain old BLOCK letters as I think it would be easy to read on my truck.

I would like to have 5 pages on my website:
1) Home
2) About Us (Know Your Poolman) / Why Hire Us
3) Services Offered
4) FAQ's
5) Contact

I am looking for a fully-functioning website (coded). Upon selection of the design winner, I am offering to increase the budget/payment by $100-$125 for the coding of all the pages. So anyone looking at participating in this contest, should be willing and able to provide the coding to the webpages that i've requested.

Target Market(s)

Upper middle-class homeowners who have a pool

Industry/Entity Type

Pool Service

Number of Pages Required

5+ page

Font styles to use
Serif

Colors
0455a3
3276b5
85acd3
85cae6
ffffff
33a6d7
0592cd

Requirements
Must have
• The Home page must have this picture highlighted in the top of the page:
• http://www.mesawaterpro.example/
• Must have pictures of some high-end pools. Any that you can find on the internet are wonderful.
• Must have a table on the right of the home page that mentions the service areas that we go to:
• • Carmel Valley (92130)
• • Del Mar (92014)
• • Rancho Santa Fe (92067)
• • Solana Beach (92075)
• • Santaluz (92127)
• • Cardiff (92007)
• • Encinitas (92024)
• • Carlsbad (92009, 92008)
• • La Jolla (92037)
• • Pacific Beach (92109)
• • Mira Mesa (92126)
• • Sorrento Valley (92121)
• • Clairemont (92117)
• • Rancho Bernardo (92127, 92128)
• • Rancho Penasquitos (92129)
• • Poway (92064)
• •
Nice to have
• Maybe incorporate some pictures of some kids (or families) playing in pools on the Why Hire Us page?
• I also like the feel of this website, but posting this page just for reference so you can get a feel more of what I like:
• http://www.crestlinepool.example/
• I like the FAQ's page from this website. I like how you can click on the question and then it pops up with the answer. http://www.dunewoodpoolcare.example/pool-spa-fountain-faqs/

```html
<!DOCTYPE html>
<html lang="en">
<head>
<meta charset="utf-8">
<title>Glimmerwave Pool Service</title>
<link href="https://fonts.googleapis.com/css2?family=Arimo:wght@400;700&family=Cinzel:wght@400;600&family=Oswald:wght@300;400&family=Roboto+Condensed:ital,wght@1,400&display=swap" rel="stylesheet">
<style>
:root{
  --navy:#1d4f94;
  --deep:#0455a3;
  --sky:#3ea5dd;
  --field:#c9e6f5;
  --footer:#2f8fc9;
  --text:#555;
  --rule:#b9b9b9;
  --white:#fff;
}
*{box-sizing:border-box;margin:0;padding:0}
html,body{width:989px;height:1200px;overflow:hidden}
body{font-family:Arimo,Arial,sans-serif;color:var(--text)}
.canvas{position:relative;width:989px;height:1200px;overflow:hidden}
.ocean{position:absolute;inset:0;background:linear-gradient(160deg,#3f8fd0 0%,#1f6fbf 35%,#2a7fcb 60%,#1b62b0 100%)}
.page{position:absolute;left:129px;top:0;width:728px;height:1110px;background:var(--white)}
.abs{position:absolute}

.brand{left:137px;top:38px;display:flex;align-items:center;gap:8px;font-family:Arimo,sans-serif;font-size:16px;font-weight:700;color:var(--deep);white-space:nowrap}
.brand .mark{width:14px;height:14px;border-radius:50%;background:var(--deep);display:block}
.call{left:696px;top:18px;display:flex;gap:7px;align-items:flex-start}
.call .label{font-size:11.5px;color:var(--navy);display:block}
.call .num{font-size:16px;font-weight:700;color:var(--navy);display:block;margin-top:1px}
.nav{top:63px;left:388px;display:flex;font-size:11.2px;color:#222}
.nav a{color:#222;text-decoration:none;padding:0 9px;border-left:1px solid #bbb;line-height:12px}
.nav a:first-child{border-left:none;position:relative}
.nav a:first-child::after{content:"";position:absolute;left:4px;right:4px;top:17px;height:2px;background:var(--navy)}

.hero{left:129px;top:106px;width:728px;height:290px;background:linear-gradient(120deg,#9fd2e8 0%,#5fb8dd 30%,#3aa0cf 55%,#7fa35a 80%,#3b5e2c 100%)}
.tagline{left:299px;top:344px;width:387px;height:38px;background:rgba(150,150,150,.75);font-family:"Roboto Condensed",sans-serif;font-style:italic;font-size:18px;color:var(--white);display:flex;align-items:center;justify-content:center}
.inquiry{left:618px;top:97px;width:195px;height:211px;background:var(--sky);border:1px solid #2f8ac3;box-shadow:0 2px 5px rgba(0,0,0,.3);padding:12px 13px}
.inquiry h2{font-size:17.5px;color:var(--white);font-weight:700;margin-bottom:8px}
.field{height:17px;background:var(--field);font-size:8px;color:#4a6a80;padding:3px 7px;margin-bottom:6px}
.field.area{height:57px}
.submit{display:inline-block;background:var(--navy);color:var(--white);font-size:11px;font-weight:700;padding:4px 7px;margin-top:1px}
.dots{left:474px;top:404px;display:flex;gap:4px}
.dots i{width:6px;height:6px;border-radius:50%;background:#aaa;display:block}
.dots i:first-child{background:var(--navy)}

.card{top:428px;width:218px;height:90px;border:1px solid #999;border-radius:6px;padding:8px 10px 0 66px}
.card svg{position:absolute;left:6px;top:10px}
.card h3{font-family:Oswald,sans-serif;font-weight:400;font-size:13.5px;color:var(--navy);margin-bottom:3px}
.card p{font-size:9.3px;line-height:14px;color:var(--text)}
.more{font-size:9.8px;color:#222;text-decoration:underline}
.card .more{position:absolute;right:12px;bottom:5px}

.h{font-family:Cinzel,serif;font-weight:600;font-size:14.5px;color:var(--navy);letter-spacing:.3px;padding-bottom:6px;border-bottom:1px dashed var(--rule)}
.copy{font-size:9.6px;line-height:14.4px;color:var(--text)}
.divider{left:606px;top:546px;width:1px;height:530px;background:#ddd}

.areas{left:143px;top:799px;display:flex;font-size:9.6px;color:var(--text)}
.areas ul{list-style:none;line-height:15.2px}
.tri{position:relative;padding-left:9px}
.tri::before{content:"";position:absolute;left:0;top:3px;border-left:4px solid var(--sky);border-top:4px solid transparent;border-bottom:4px solid transparent}

.review{left:143px;width:430px;font-size:9.6px;line-height:15.4px;color:#333}
.q{font-family:Georgia,serif;font-size:30px;color:#aaa;font-weight:700;line-height:0;vertical-align:-11px}

.svc{left:626px;top:651px;width:212px;list-style:none;font-size:9.4px;line-height:13.8px;color:var(--text)}
.svc li{padding-left:13px;margin-bottom:2.6px}
.svc li::before{top:3px}

.foot{left:127px;top:1109px;width:730px;height:91px;background:var(--footer);color:var(--white)}
.fnav{left:15px;top:21px;display:flex;font-size:9.8px}
.fnav span{padding:0 8px;border-left:1px solid rgba(255,255,255,.7)}
.fnav span:first-child{border-left:none;padding-left:0;padding-right:15px}
.faddr{left:20px;top:40px;font-size:10.3px}
.fcopy{left:0;width:730px;top:69px;text-align:center;font-size:8.6px}
.follow{left:458px;top:22px;font-size:10.2px}
.social{left:459px;top:38px;display:flex;gap:8px}
.social i{width:18px;height:18px;background:#e9f3fa;border-radius:2px;display:block}
.fbrand{left:592px;top:30px;width:130px;text-align:right;font-family:Arimo,sans-serif;font-weight:700;font-size:11px;line-height:14px;color:var(--white)}
</style>
</head>
<body>
<div class="canvas">
  <div class="ocean" role="img" aria-label="Deep blue ocean water surface"></div>
  <div class="page"></div>

  <div class="abs brand"><i class="mark"></i>Glimmerwave Pool Service</div>

  <div class="abs call">
    <svg width="24" height="24" viewBox="0 0 24 24" aria-hidden="true"><circle cx="12" cy="12" r="10.5" fill="none" stroke="#1d4f94" stroke-width="1.5"/><path d="M9 6.5c-1 .6-1.6 2-1 4 .8 2.8 2.8 5.4 5 6.6 1.4.7 2.6.3 3.2-.4l-1.8-2-1.4.6c-1.2-.8-2.2-2.2-2.7-3.6l1.2-.9-1-2.8z" fill="#1d4f94"/></svg>
    <div><span class="label">Call Us Today</span><span class="num">555-014-2290</span></div>
  </div>

  <nav class="abs nav">
    <a>Home</a><a>About Us</a><a>Services Offered</a><a>FAQ’s</a><a>Why Hire Us</a><a>Contact Us</a>
  </nav>

  <div class="abs hero" role="img" aria-label="High-end swimming pool with fountain columns, clear blue water and palm trees"></div>
  <div class="abs tagline">Water so pure, it sparkles like a summer sky.</div>

  <form class="abs inquiry">
    <h2>Quick Inquiry</h2>
    <div class="field">Name</div>
    <div class="field">Email</div>
    <div class="field">Mobile</div>
    <div class="field area">Questions / Comments</div>
    <span class="submit">Submit</span>
  </form>

  <div class="abs dots"><i></i><i></i><i></i><i></i><i></i></div>

  <div class="abs card" style="left:143px">
    <svg width="50" height="44" viewBox="0 0 50 44" aria-hidden="true"><path d="M2 20 L18 6 L34 20 H30 V36 H6 V20z" fill="#1d4f94"/><rect x="14" y="26" width="7" height="10" fill="#fff"/><path d="M30 28h16M30 33h16M30 38h16" stroke="#1d4f94" stroke-width="2"/><path d="M38 20v18M44 20v18" stroke="#1d4f94" stroke-width="1.6"/></svg>
    <h3>Residential Services</h3>
    <p>Glimmerwave Pool Service offers maintenance and repairs for all residential pools.</p>
    <span class="more">Read More</span>
  </div>
  <div class="abs card" style="left:383px">
    <svg width="50" height="44" viewBox="0 0 50 44" aria-hidden="true"><rect x="4" y="14" width="8" height="22" fill="#1d4f94"/><rect x="14" y="4" width="8" height="32" fill="#1d4f94"/><rect x="24" y="18" width="6" height="18" fill="#1d4f94"/><path d="M2 36h46M30 30h16M30 35h16M30 40h16" stroke="#1d4f94" stroke-width="2"/><path d="M38 22v18M44 22v18" stroke="#1d4f94" stroke-width="1.6"/></svg>
    <h3>Commercial Services</h3>
    <p>we do it all! Health Clubs, Schools, Hotels, Motels, Apartments, Condominiums</p>
    <span class="more">Read More</span>
  </div>
  <div class="abs card" style="left:622px">
    <svg width="36" height="36" viewBox="0 0 24 24" aria-hidden="true"><circle cx="12" cy="12" r="10.5" fill="none" stroke="#1d4f94" stroke-width="1.3"/><path d="M9 6.5c-1 .6-1.6 2-1 4 .8 2.8 2.8 5.4 5 6.6 1.4.7 2.6.3 3.2-.4l-1.8-2-1.4.6c-1.2-.8-2.2-2.2-2.7-3.6l1.2-.9-1-2.8z" fill="#1d4f94"/></svg>
    <h3>Quick Inquiry</h3>
    <p>Please call or E-Mail us with any questions about our pool service, or to schedule a free pool...</p>
    <span class="more">Read More</span>
  </div>

  <h2 class="abs h" style="left:143px;top:548px;width:427px">WELCOME TO GLIMMERWAVE POOL SERVICE</h2>
  <p class="abs copy" style="left:143px;top:583px;width:450px">At Glimmerwave Pool Service, we understand that your pool is an important investment. Whether it’s part of your business or in your backyard, it needs to be well taken care of to ensure its longevity and your peace of mind. At Glimmerwave Pool Service, we pride ourselves in setting the standard in our industry. What sets us apart from our competition is our commitment to excellence. Our exceptional service and competitive price make us the clear choice for your pool service needs.</p>
  <p class="abs copy" style="left:143px;top:668px;width:450px">Glimmerwave Pool Service has been providing spectacular pool &amp; spa cleaning and maintenance service for over 7 years.  Our technicians are professionally trained and are committed to providing outstanding customer service through our honest...</p>
  <span class="abs more" style="left:143px;top:716px;font-size:10.3px">Read More</span>

  <div class="abs divider"></div>

  <h2 class="abs h" style="left:143px;top:766px;width:427px">SERVICE AREAS THAT WE GO TO:</h2>
  <div class="abs areas">
    <ul style="width:154px">
      <li class="tri">Carmel Valley (92130)</li><li class="tri">Del Mar (92014)</li><li class="tri">Rancho Santa Fe (92067)</li><li class="tri">Solana Beach (92075)</li><li class="tri">Santaluz (92127)</li><li class="tri">Cardiff (92007)</li>
    </ul>
    <ul style="width:148px">
      <li class="tri">Mira Mesa (92126)</li><li class="tri">Encinitas (92024)</li><li class="tri">Carlsbad (92009, 92008)</li><li class="tri">La Jolla (92037)</li><li class="tri">Pacific Beach (92109)</li>
    </ul>
    <ul>
      <li class="tri">Sorrento Valley (92121)</li><li class="tri">Clairemont (92117)</li><li class="tri">Rancho Bernardo (92127, 92128)</li><li class="tri">Rancho Penasquitos (92129)</li><li class="tri">Poway (92064)</li>
    </ul>
  </div>

  <h2 class="abs h" style="left:143px;top:918px;width:427px">CUSTOMER REVIEWS</h2>
  <p class="abs review" style="top:952px"><span class="q">“</span> Working with Marco is terrific.  His education and professional background sets him apart from all the other pool cleaners.  He has excellent communication with us and he shows up when he says he will. Glimmerwave is the only pool care company I have ever recommended to my friends <span class="q">”</span></p>
  <p class="abs review" style="top:1013px"><span class="q">“</span> I was looking for a pool service company and I’m so glad I found Glimmerwave! Marco, the owner, is an honest business man.Don’t go anywhere else!  You’ll be surprised at what a great communicator Marco is and the service that he does is awesome! <span class="q">”</span></p>
  <span class="abs more" style="left:144px;top:1067px;font-size:10.3px">Read More</span>

  <h2 class="abs h" style="left:626px;top:548px;width:206px">SERVICES OFFERED</h2>
  <p class="abs copy" style="left:626px;top:577px;width:212px;font-size:9.3px;line-height:12.5px">Glimmerwave Pool Service is a full service company. We cover the complete spectrum of regular service and repair. From start-ups to restoring swampy pools, repairing or replacing equipment, Glimmerwave does it all</p>
  <ul class="abs svc">
    <li class="tri">Swimming Pool and Spa Cleaning</li>
    <li class="tri">Install and repair lighting</li>
    <li class="tri">New Pool and Spa Start Ups</li>
    <li class="tri">Leak Detection &amp; Salt System Conversions</li>
    <li class="tri">Troubleshoot and Repair pumps, filters, heaters and heat exchangers</li>
    <li class="tri">Fountain Cleaning and Service</li>
    <li class="tri">Tile Cleaning &amp; Restoration</li>
    <li class="tri">Licensed and Bonded Swimming Pool Technicians</li>
    <li class="tri">CPO (Certified Pool Operator) Insured</li>
    <li class="tri">Low Rates for Repairs, Maintenance, Cleaning</li>
    <li class="tri">Reliable &amp; affordable pool &amp; spa maintenance</li>
    <li class="tri">Friendly assistance from the staff</li>
    <li class="tri">Brushing walls and tile cleaning</li>
    <li class="tri">Salt water system maintenance</li>
    <li class="tri">Pool leakage detection and repairs</li>
    <li class="tri">Noisy pool motor repairs</li>
    <li class="tri">Prompt swimming pool cleaning each week Vacuuming pool floor and steps</li>
    <li class="tri">Eliminating leaves and debris</li>
    <li class="tri">Cleaning out debris in skimmer and pool pump basket</li>
    <li class="tri">Making your pool and spa crystal clear with balanced chemicals</li>
  </ul>
  <span class="abs more" style="left:795px;top:1068px;font-size:10.3px">Read More</span>

  <footer class="abs foot">
    <div class="abs fnav"><span>Home</span><span>About Us</span><span>Services Offered</span><span>FAQ’s</span><span>Why Hire Us</span><span>Contact Us</span></div>
    <div class="abs faddr">Street Name City Name State Zipcode &nbsp;|&nbsp;  Phone: 555-014-2290</div>
    <div class="abs follow">Follow Us On</div>
    <div class="abs social"><i></i><i></i><i></i></div>
    <div class="abs fbrand">Glimmerwave Pool Service</div>
    <div class="abs fcopy">Copyright © 2015,  GlimmerwavePoolService.com  |  All Rights Reserved.</div>
  </footer>
</div>
</body>
</html>
```